Private Security Company Business Card and Logo Design

Looking for a modern conservative business card design for our new private security company Halvern Guard Partners, Inc. or HGP for short.
Private Security Services. The current logo we have is not very good and honestly would like a sharp logo for the card instead of using the one we have now. Open to ideas. I am easy just looking for something nicer then what I can personally design on cardloomix. I searched on zintrova for Security Company business cards went to images and found some nice designs that were made here.

Target Market(s)

Security Services

Industry/Entity Type

Business

Contact Information for Business Card

Halvern Guard Partners, Inc.
President, cell,office,fax,email, website,
Logo etc, whatever is needed for a standard business card
Can provide personal Information later.

Colors
0556a4
ffffff
474747

Requirements
Must have
• Modern but conservative,
Nice to have
• color choices
• Blue, white, Grey

```html
<!DOCTYPE html>
<html lang="en">
<head>
<meta charset="utf-8">
<title>Halvern Guard Partners, Inc. — Business Card</title>
<link rel="stylesheet" href="https://fonts.googleapis.com/css2?family=Orbitron:wght@500&family=Noto+Sans:ital,wght@0,400;1,400&display=swap">
<style>
  :root {
    --page-bg: #ffffff;
    --card-center: #2b2b2b;
    --card-mid: #1d1d1d;
    --card-edge: #121212;
    --brand-blue: #7fb6e4;
    --brand-blue-light: #a9d2f2;
    --brand-blue-deep: #5c9bd3;
    --text-light: #e6e6e6;
  }
  * { box-sizing: border-box; margin: 0; padding: 0; }
  html, body {
    width: 1021px;
    height: 1200px;
    overflow: hidden;
    background: var(--page-bg);
  }
  .sheet {
    position: relative;
    width: 1021px;
    height: 1200px;
  }
  .card {
    position: absolute;
    left: 53px;
    width: 873px;
    height: 512px;
    background: radial-gradient(ellipse at 50% 50%, var(--card-center) 0%, var(--card-mid) 55%, var(--card-edge) 100%);
    box-shadow: 14px 16px 26px rgba(0, 0, 0, 0.45);
    overflow: hidden;
  }
  .card--front { top: 52px; }
  .card--back { top: 596px; }

  .company-name {
    position: absolute;
    left: 0;
    width: 100%;
    text-align: center;
    font-family: "Orbitron", sans-serif;
    font-weight: 500;
    font-size: 35px;
    letter-spacing: 1px;
    color: var(--brand-blue);
    background: linear-gradient(180deg, var(--brand-blue-light) 0%, var(--brand-blue) 50%, var(--brand-blue-deep) 100%);
    -webkit-background-clip: text;
    background-clip: text;
    -webkit-text-fill-color: transparent;
  }
  .card--front .company-name { top: 60px; }
  .card--back .company-name { top: 220px; }

  .holder {
    position: absolute;
    top: 206px;
    left: 0;
    width: 100%;
    text-align: center;
    font-family: "Noto Sans", sans-serif;
  }
  .holder__name {
    font-size: 30px;
    font-variant: small-caps;
    letter-spacing: 1px;
    color: var(--brand-blue);
    line-height: 38px;
  }
  .holder__title {
    font-size: 24px;
    font-style: italic;
    color: var(--text-light);
    line-height: 32px;
  }

  .contact-lines {
    position: absolute;
    top: 366px;
    left: 43px;
    font-family: "Noto Sans", sans-serif;
    font-size: 24px;
    color: var(--text-light);
    list-style: none;
  }
  .contact-lines li {
    display: flex;
    align-items: center;
    gap: 8px;
    height: 38px;
  }
  .contact-lines svg { width: 26px; height: 22px; fill: var(--brand-blue); }

  .location {
    position: absolute;
    top: 366px;
    right: 41px;
    text-align: right;
    font-family: "Noto Sans", sans-serif;
    color: var(--text-light);
  }
  .location__web { font-size: 25px; line-height: 38px; }
  .location__address { font-size: 21px; font-style: italic; line-height: 38px; }
</style>
</head>
<body>
<main class="sheet">

  <section class="card card--front">
    <h1 class="company-name">HALVERN GUARD PARTNERS, INC.</h1>

    <div class="holder">
      <p class="holder__name">Dorian Weller</p>
      <p class="holder__title">President</p>
    </div>

    <ul class="contact-lines">
      <li>
        <svg viewBox="0 0 26 22" aria-label="Phone" role="img">
          <path d="M2 6 C2 2 24 2 24 6 L24 8 L18 8 L18 6 C14 5 12 5 8 6 L8 8 L2 8 Z"/>
          <path d="M6 10 L20 10 L24 19 L2 19 Z M10 12 L10 14 L12 14 L12 12 Z M14 12 L14 14 L16 14 L16 12 Z M10 15 L10 17 L12 17 L12 15 Z M14 15 L14 17 L16 17 L16 15 Z"/>
        </svg>
        <span>(555) 318-2740</span>
      </li>
      <li>
        <svg viewBox="0 0 26 22" aria-label="Fax" role="img">
          <path d="M8 1 L20 1 L20 8 L8 8 Z"/>
          <path d="M2 9 L24 9 L24 21 L2 21 Z M5 11 L5 19 L8 19 L8 11 Z M11 12 L11 14 L21 14 L21 12 Z M11 16 L11 18 L21 18 L21 16 Z" fill-rule="evenodd"/>
        </svg>
        <span>(555) 318-2749</span>
      </li>
    </ul>

    <div class="location">
      <p class="location__web">www.halvernguard.com</p>
      <p class="location__address">18 Ashcombe Ave, Lakeford, ST 40712</p>
    </div>
  </section>

  <section class="card card--back">
    <h2 class="company-name">HALVERN GUARD PARTNERS, INC.</h2>
  </section>

</main>
</body>
</html>
```